7 Elite Label

Design a label for 7 Elite styling gels. The logo is attached. The color is C=100, M=100, Y=0, K=0. The 16 oz. jar is also attached.

Updates

Attention all designers,

The old logo has been deleted.  I have uploaded a new logo for this project.  Can you please update your design with the NEW LOGO?
thank you,
Rob

Target Market(s)

Multicultural

Requirements
Must have
• you must used the logo attached.

text to be included on the jar:

Used by Professionals
Maximum Hold
Alcohol Free
NO FLAKING

16 oz.

As far as label size, use the jar photo, and fit the design on it.

```html
<!DOCTYPE html>
<html lang="en">
<head>
<meta charset="utf-8">
<title>7 Elite Label – Two Variants</title>
<link rel="stylesheet" href="https://fonts.googleapis.com/css2?family=Libre+Baskerville:wght@400;700&display=swap">
<style>
  :root {
    --label-blue: #12289a;
    --label-white: #ffffff;
    --page: #ffffff;
  }
  html, body {
    margin: 0;
    padding: 0;
    width: 1200px;
    height: 1000px;
    overflow: hidden;
    background: var(--page);
  }
  .sheet {
    display: block;
    width: 1200px;
    height: 1000px;
  }
  .label-text {
    font-family: "Libre Baskerville", "Times New Roman", serif;
    font-weight: 700;
  }
  .ink-blue { fill: var(--label-blue); }
  .ink-white { fill: var(--label-white); }
  .tagline { font-size: 16.5px; letter-spacing: 0.3px; }
  .hold { font-size: 18.5px; }
  .claim { font-size: 15.5px; }
  .size { font-size: 18px; font-weight: 400; }
  .brand-name { font-size: 30px; }
  .rule { fill: var(--label-blue); }
  .band { fill: var(--label-blue); }
</style>
</head>
<body>
<svg class="sheet" viewBox="0 0 1200 1000" xmlns="http://www.w3.org/2000/svg">

  <g class="label label--underlined">
    <text class="label-text tagline ink-blue" x="358" y="148" text-anchor="middle">USED BY PROFESSIONALS</text>
    <rect class="rule" x="232" y="157" width="252" height="6"/>
    <text class="label-text hold ink-blue" x="360" y="191" text-anchor="middle">Maximum Hold</text>

    <path class="band" d="M200,325 C250,318 300,270 360,240 C420,208 470,188 515,183 L515,388 L200,388 Z"/>

    <text class="label-text claim ink-blue" transform="translate(226,314) rotate(-31)">NO FLAKING</text>
    <text class="label-text size ink-white" x="284" y="334">16 oz.</text>

    <text class="label-text brand-name ink-white" x="443" y="342" text-anchor="middle">7 Elite</text>
  </g>

  <g class="label label--angled">
    <text class="label-text tagline ink-blue" x="835" y="147" text-anchor="middle">USED BY PROFESSIONALS</text>

    <path class="band" d="M686,325 C730,318 770,290 820,262 C880,228 935,200 984,192 L984,386 L686,386 Z"/>

    <text class="label-text hold ink-blue" transform="translate(822,250) rotate(-25)">Maximum Hold</text>
    <text class="label-text claim ink-blue" transform="translate(691,321) rotate(-25)">NO FLAKING</text>
    <text class="label-text size ink-white" x="766" y="334">16 oz.</text>

    <text class="label-text brand-name ink-white" x="914" y="342" text-anchor="middle">7 Elite</text>
  </g>

</svg>
</body>
</html>
```